Inspiration Poster

Inspirational Poster that has a Kamran Dulo like abstract look (http://www.vexalo.com/images/search?q=kamran+dulo&FORM=HDRSC2) with the text:

"we walk not in order to arrive at the promise land but because walking itself is a revolution"
-Peter Ambrick

```html
<!DOCTYPE html>
<html lang="en">
<head>
<meta charset="utf-8">
<title>Inspiration Poster</title>
<link rel="stylesheet" href="https://fonts.googleapis.com/css2?family=Open+Sans:wght@400;500&display=swap">
<style>
  :root {
    --umber: #4a3a33;
    --slate: #6f6259;
    --rust: #b86448;
    --clay: #d08f63;
    --ochre: #c9a464;
    --mauve: #8e6673;
    --plum: #6c4f5a;
    --quote: #f4e7c3;
    --byline: #f5efe2;
  }
  html, body {
    margin: 0;
    padding: 0;
    overflow: hidden;
  }
  body {
    width: 848px;
    height: 1200px;
    background: var(--umber);
  }
  .poster {
    position: relative;
    width: 848px;
    height: 1200px;
    overflow: hidden;
  }
  .rock-surface {
    position: absolute;
    inset: 0;
    background:
      radial-gradient(ellipse 30% 14% at 18% 6%, rgba(201,164,100,0.5), transparent 70%),
      radial-gradient(ellipse 50% 22% at 70% 22%, rgba(111,98,89,0.7), transparent 70%),
      radial-gradient(ellipse 55% 20% at 45% 58%, rgba(208,143,99,0.9), transparent 72%),
      radial-gradient(ellipse 35% 22% at 88% 62%, rgba(184,100,72,0.85), transparent 70%),
      radial-gradient(ellipse 30% 18% at 10% 48%, rgba(184,100,72,0.6), transparent 70%),
      radial-gradient(ellipse 55% 25% at 35% 90%, rgba(142,102,115,0.85), transparent 72%),
      radial-gradient(ellipse 30% 18% at 88% 92%, rgba(201,164,100,0.5), transparent 70%),
      linear-gradient(170deg, var(--umber) 0%, var(--slate) 20%, var(--mauve) 40%, var(--rust) 62%, var(--plum) 82%, var(--mauve) 100%);
  }
  .quote {
    position: absolute;
    left: 28px;
    top: 64px;
    margin: 0;
    font-family: "Open Sans", sans-serif;
    font-weight: 500;
    font-size: 50px;
    line-height: 58px;
    letter-spacing: 0.5px;
    color: var(--quote);
    text-shadow: 0 1px 3px rgba(40,20,10,0.55);
    white-space: nowrap;
  }
  .quote-line { display: block; }
  .attribution {
    position: absolute;
    right: 158px;
    top: 292px;
    margin: 0;
    font-family: "Open Sans", sans-serif;
    font-weight: 400;
    font-size: 37px;
    letter-spacing: 0.5px;
    color: var(--byline);
    text-shadow: 0 1px 3px rgba(40,20,10,0.55);
    white-space: nowrap;
  }
</style>
</head>
<body>
  <main class="poster">
    <div class="rock-surface" role="img" aria-label="Abstract weathered rock surface with a crack, in rust, ochre and mauve tones"></div>
    <blockquote class="quote">
      <span class="quote-line">"We walk not in order to</span>
      <span class="quote-line">arrive at the promise land</span>
      <span class="quote-line">but because walking itself</span>
      <span class="quote-line">is a revolution"</span>
    </blockquote>
    <p class="attribution">–Peter Ambrick</p>
  </main>
</body>
</html>
```